Laptop Accessories Packing Design

We are looking for a new package design of a laptop accesories (batteries, charges, hard drives etc.). We want to refresh our brand Vireo CellWorks. At VireoCell, we create high-end laptop accessories that ensure reliability, performance, and longevity for users worldwide. Our mission is to deliver innovative and durable solutions that allow users to work, create, and grow without limits.
General Packaging Concept
Minimalist and elegant look, yet with elements that catch the eye (Vireo products will mainly be offered on auction portals such as Brindle, Kiva, Tollmart, so it would be good if the packaging attracted attention and stood out from the competitors).
Should I put a photo, sketch or product icon on the box? We'll leave that to your imagination.
We ask for a general design of the packaging. After the competition, together with the winner, we will add the rest of the information to the back and sides of the box.
In the attachments there is our Logo (you can use other colors) and sample packaging of competitors
Target Market(s)
E-commerse
Industry/Entity Type
individual end customer
Look and feel
Each slider illustrates characteristics of the customer's brand and the style your logo design should communicate.

```html
<!DOCTYPE html>
<html lang="en">
<head>
<meta charset="utf-8">
<title>Vireo Laptop Battery Packaging</title>
<link href="https://fonts.googleapis.com/css2?family=Montserrat:wght@800;900&family=Oswald:wght@400&display=swap" rel="stylesheet">
<style>
  :root {
    --page-bg: #ececec;
    --box-black: #070707;
    --box-charcoal: #1a1a1a;
    --gold: #d4a22a;
    --gold-light: #f2c94c;
    --gold-deep: #a8771a;
    --white: #ffffff;
    --icon-grey: #d9d9d9;
  }
  * { margin: 0; padding: 0; box-sizing: border-box; }
  html, body { width: 1200px; height: 800px; overflow: hidden; }
  body {
    background: var(--page-bg);
    display: flex; align-items: center; justify-content: center;
    font-family: "Montserrat", sans-serif;
  }
  .box-front {
    position: relative;
    width: 1120px; height: 584px;
    background: radial-gradient(ellipse at 55% 70%, var(--box-charcoal), var(--box-black) 65%);
    overflow: hidden;
  }
  .hero-visual {
    position: absolute; right: 0; top: 0;
    width: 680px; height: 584px;
    background:
      radial-gradient(ellipse 40% 30% at 58% 50%, rgba(242,201,76,0.85), rgba(168,119,26,0.35) 55%, transparent 80%),
      radial-gradient(ellipse 45% 40% at 88% 15%, rgba(242,201,76,0.75), rgba(168,119,26,0.2) 60%, transparent 85%),
      linear-gradient(90deg, transparent, rgba(0,0,0,0) 20%);
  }
  .brand-name {
    position: absolute; left: 70px; top: 50px;
    font-weight: 900; font-size: 64px; color: var(--white);
    letter-spacing: 1px;
  }
  .product-title {
    position: absolute; left: 80px; top: 222px;
    font-weight: 900; font-size: 90px; line-height: 80px; letter-spacing: 1px;
  }
  .product-title .line-laptop { display: block; color: var(--white); }
  .product-title .line-battery {
    display: block;
    background: linear-gradient(180deg, var(--gold-light), var(--gold-deep));
    -webkit-background-clip: text; background-clip: text; color: transparent;
  }
  .tagline-pill {
    position: absolute; left: 70px; top: 398px;
    width: 290px; height: 49px; border-radius: 25px;
    background: linear-gradient(180deg, var(--gold-light), var(--gold-deep));
    border: 2px solid #f5e2a8;
    display: flex; align-items: center; justify-content: center;
    font-family: "Oswald", sans-serif; font-size: 21px; color: var(--white);
  }
  .cert-badges {
    position: absolute; left: 84px; top: 508px;
    display: flex; gap: 14px; align-items: center;
  }
  .cert-badge { width: 38px; height: 34px; border: 2px solid var(--icon-grey); border-radius: 4px; }
  .cert-badge.round { border-radius: 50%; width: 34px; }
  .corner-lines { position: absolute; inset: 0; }
</style>
</head>
<body>
  <main class="box-front">
    <div class="hero-visual" role="img" aria-label="Laptop on a dark hexagon-textured surface with golden light streaks and sparks"></div>

    <svg class="corner-lines" width="1120" height="584" viewBox="0 0 1120 584" aria-hidden="true">
      <line x1="838" y1="0" x2="1120" y2="288" stroke="var(--white)" stroke-width="3"/>
      <polygon points="985,584 1120,448 1120,584" fill="var(--box-black)"/>
      <line x1="983" y1="584" x2="1120" y2="446" stroke="var(--white)" stroke-width="3"/>
    </svg>

    <div class="brand-name">Vireo</div>

    <h1 class="product-title">
      <span class="line-laptop">LAPTOP</span>
      <span class="line-battery">BATTERY</span>
    </h1>

    <div class="tagline-pill">HIGH-END LAPTOP ACCESSORIES</div>

    <div class="cert-badges" aria-label="Certification marks">
      <span class="cert-badge"></span>
      <span class="cert-badge round"></span>
      <span class="cert-badge round"></span>
      <span class="cert-badge"></span>
      <span class="cert-badge"></span>
    </div>
  </main>
</body>
</html>
```